PLUM BUSINESS CARD

Need a business card and logo. The company name is PLUM (Piedmont League of Ultimate Mareriders). It's a business that offers horseback riding lessons to young girls. Please put my name: Renata Bowley and a place for email and phone number. I would like the card to look feminine and soft. I like script type lettering. I want the card to be white or ivory with black or gray and hot pink print. A horse head outline would be cool, something whimsical. Think teen girl who likes glamour. Also, I give western riding lessons. So I like faded out background Images of western saddles, cowgirls, horses with long hair, ropes, horses in sunset...mabe the word PLUM can be made out of a lasso rope?

Just updated my project with a little more detail

Target Market(s)

Young girls/ cowgirls, western riding

Industry/Entity Type

Horseback Riding

Font styles to use
Script

Colors
e34197

Requirements
Must have
• A logo of PLUM.
Must say Piedmont League of Ultimate Mareriders
Colors are Pink and Black with an elegant, glamorous, feminine look.
Nice to have
• Could have a picture or outline of a horse

```html
<!DOCTYPE html>
<html lang="en">
<head>
<meta charset="utf-8">
<title>PLUM Business Card</title>
<link rel="stylesheet" href="https://fonts.googleapis.com/css2?family=Lobster+Two:ital,wght@0,700;1,400;1,700&display=swap">
<style>
  :root {
    --stage: #f2f2f2;
    --sky-top: #b0237f;
    --sky-mid: #d95aae;
    --horizon: #f6d3ea;
    --ground: #8a1460;
    --ground-deep: #5e0b41;
    --logo-tint: #f1c6e6;
    --ink: #1a0a14;
    --ink-soft: #3a0c2a;
    --paper: #ffffff;
  }
  * { margin: 0; padding: 0; box-sizing: border-box; }
  html, body {
    width: 1200px;
    height: 900px;
    overflow: hidden;
    background: var(--stage);
  }
  .business-card {
    position: absolute;
    left: 100px;
    top: 164px;
    width: 1000px;
    height: 572px;
    border-radius: 40px;
    overflow: hidden;
    box-shadow: 0 18px 40px rgba(60, 10, 40, 0.25);
  }
  .card-scene {
    position: absolute;
    inset: 0;
    background:
      radial-gradient(ellipse 60% 18% at 62% 52%, rgba(255,240,250,0.9), rgba(255,240,250,0) 100%),
      linear-gradient(180deg,
        var(--sky-top) 0%,
        var(--sky-mid) 30%,
        var(--horizon) 50%,
        var(--sky-mid) 60%,
        var(--ground) 74%,
        var(--ground-deep) 100%);
  }
  .brand {
    position: absolute;
    left: 56px;
    top: 44px;
    display: flex;
    align-items: center;
    gap: 18px;
  }
  .brand-dot {
    width: 54px;
    height: 54px;
    border-radius: 50%;
    background: var(--logo-tint);
  }
  .brand-name {
    font-family: "Lobster Two", cursive;
    font-weight: 700;
    font-style: normal;
    font-size: 150px;
    line-height: 1;
    color: var(--logo-tint);
    letter-spacing: 4px;
  }
  .contact {
    position: absolute;
    left: 290px;
    top: 268px;
    font-family: "Lobster Two", cursive;
    font-style: italic;
  }
  .contact-name {
    font-weight: 700;
    font-size: 40px;
    color: var(--ink);
    letter-spacing: 1px;
  }
  .contact-phone {
    margin-top: 6px;
    font-weight: 400;
    font-size: 38px;
    color: var(--ink-soft);
    letter-spacing: 2px;
  }
  .contact-email {
    margin-top: 8px;
    font-weight: 400;
    font-size: 32px;
    color: var(--ink-soft);
  }
  .tagline {
    position: absolute;
    left: 40px;
    right: 40px;
    bottom: 48px;
    font-family: "Lobster Two", cursive;
    font-weight: 700;
    font-style: italic;
    font-size: 36px;
    color: var(--paper);
    letter-spacing: 1px;
    text-align: center;
    transform: rotate(-2deg);
  }
</style>
</head>
<body>
  <main class="business-card">
    <div class="card-scene" role="img" aria-label="Sunset prairie in magenta tones with a cowgirl riding a galloping horse in silhouette on the right"></div>

    <div class="brand">
      <span class="brand-dot"></span>
      <span class="brand-name">PLUM</span>
    </div>

    <div class="contact">
      <p class="contact-name">Renata Bowley</p>
      <p class="contact-phone">1472 836 519</p>
      <p class="contact-email">renata@plumriders.com</p>
    </div>

    <p class="tagline">Piedmont League of Ultimate Mareriders</p>
  </main>
</body>
</html>
```